High Quality Business card for Property Management Agency - Super Classy and professional design

High Quality Business card design.

We need a business card designed for our Property Management Agency.
We are located on Sydney's Northern Beaches and manage beautiful properties along the beach and harbor.
We need a design that oozes modern, classy and professional.
I would like it to be double sided with contact details and logo on the front and just the logo on the back.

I need a print ready PDF version of the file as well as an editable photoshop (PSD) version of the file.

Logo and information details attached.

Target Market(s)

Property owners/investors, Male and Female Aged 28-65

Industry/Entity Type

Real Estate

Contact Information for Business Card

Tom Carrick
Tel: 0467 239 018
Email: tom@harvestlaneestates.com.au
Website: www.harvestlaneestates.com.au
Address: Level 2, 17 Wattlecourt Rd, Dunmarra NSW 2187

Font styles to use
Sans Serif

Requirements
Must have
• - Logo front and back
• - Business card details listed above and attached
• - Colour
Nice to have
• Sleek and professional

```html
<!DOCTYPE html>
<html lang="en">
<head>
<meta charset="utf-8">
<title>Harvest Lane Estates – Business Card</title>
<link rel="stylesheet" href="https://fonts.googleapis.com/css2?family=Open+Sans:wght@400;600&family=PT+Sans:wght@700&display=swap">
<style>
  :root {
    --page: #ece7e1;
    --card-navy: #1f4396;
    --wave-deep: #2566b8;
    --wave-mid: #2f8fd3;
    --wave-light: #4cc3ec;
    --wave-pale: #8fe3f7;
    --highlight: #b7ecfa;
    --accent-teal: #2fa6a0;
    --icon-blue: #5bc0ef;
    --text-light: #f2f5ff;
    --text-dark: #0b0f1c;
  }
  * { box-sizing: border-box; margin: 0; padding: 0; }
  html, body {
    width: 1200px; height: 729px; overflow: hidden;
    background: var(--page);
    font-family: "Open Sans", Arial, sans-serif;
  }
  .sheet {
    position: relative; width: 1200px; height: 729px;
    display: flex; align-items: center; justify-content: center; gap: 50px;
  }
  .card {
    position: relative; width: 540px; height: 310px;
    background: var(--card-navy);
    border-radius: 26px 26px 4px 4px;
    overflow: hidden;
    box-shadow: 0 6px 18px rgba(0,0,0,0.18);
  }
  .card__waves { position: absolute; inset: 0; width: 100%; height: 100%; }
  .brand {
    position: absolute; display: flex; align-items: center; gap: 12px;
    color: var(--text-light); font-family: "Open Sans", Arial, sans-serif;
    font-weight: 600; letter-spacing: 0.02em; white-space: nowrap;
  }
  .brand__dot { border-radius: 50%; background: var(--accent-teal); flex: none; }
  .card--back .brand { left: 0; right: 0; top: 92px; justify-content: center; font-size: 38px; }
  .card--back .brand__dot { width: 26px; height: 26px; }
  .card--front .brand { right: 26px; top: 28px; font-size: 20px; gap: 8px; }
  .card--front .brand__dot { width: 14px; height: 14px; }
  .contact-list {
    position: absolute; left: 32px; top: 86px; list-style: none;
    color: var(--text-light); font-size: 14.5px;
  }
  .contact-list li { display: flex; align-items: center; gap: 12px; height: 34px; }
  .contact-list svg { width: 20px; height: 20px; flex: none; }
  .holder-name {
    position: absolute; right: 34px; bottom: 22px;
    font-family: "PT Sans", Arial, sans-serif; font-weight: 700;
    font-size: 34px; color: var(--text-dark); letter-spacing: 0.02em;
  }
</style>
</head>
<body>
<main class="sheet">

  <section class="card card--back" aria-label="Card back">
    <svg class="card__waves" viewBox="0 0 540 310" preserveAspectRatio="none" aria-hidden="true">
      <defs>
        <linearGradient id="backPale" x1="0" y1="0" x2="0" y2="1">
          <stop offset="0" stop-color="var(--wave-light)"/>
          <stop offset="1" stop-color="var(--wave-pale)"/>
        </linearGradient>
      </defs>
      <path d="M0 200 C160 185 340 170 540 140 L540 310 L0 310Z" fill="var(--wave-deep)"/>
      <path d="M0 232 C180 215 360 200 540 178 L540 310 L0 310Z" fill="var(--wave-mid)"/>
      <path d="M120 232 C260 222 400 206 540 188" fill="none" stroke="var(--highlight)" stroke-width="4"/>
      <path d="M0 268 C180 250 380 238 540 236 L540 310 L0 310Z" fill="url(#backPale)"/>
    </svg>
    <div class="brand"><span class="brand__dot"></span>HARVEST LANE ESTATES</div>
  </section>

  <section class="card card--front" aria-label="Card front">
    <svg class="card__waves" viewBox="0 0 540 310" preserveAspectRatio="none" aria-hidden="true">
      <defs>
        <linearGradient id="frontPale" x1="0" y1="0" x2="0" y2="1">
          <stop offset="0" stop-color="var(--wave-light)"/>
          <stop offset="1" stop-color="var(--wave-pale)"/>
        </linearGradient>
      </defs>
      <path d="M0 222 C150 212 300 200 540 208 L540 310 L0 310Z" fill="var(--wave-deep)"/>
      <path d="M0 246 C160 238 300 222 540 224 L540 310 L0 310Z" fill="var(--wave-mid)"/>
      <path d="M0 258 C120 256 230 248 330 232" fill="none" stroke="var(--highlight)" stroke-width="5"/>
      <path d="M0 280 C200 268 360 250 540 262 L540 310 L0 310Z" fill="url(#frontPale)"/>
    </svg>

    <div class="brand"><span class="brand__dot"></span>HARVEST LANE ESTATES</div>

    <ul class="contact-list">
      <li>
        <svg viewBox="0 0 20 20" aria-hidden="true"><path d="M10 2 L19 10 H16 V18 H12 V13 H8 V18 H4 V10 H1Z" fill="var(--icon-blue)"/></svg>
        Level 2, 17 Wattlecourt Rd, Dunmarra NSW 2187
      </li>
      <li>
        <svg viewBox="0 0 20 20" aria-hidden="true" fill="none" stroke="var(--icon-blue)" stroke-width="1.5"><circle cx="10" cy="10" r="8"/><ellipse cx="10" cy="10" rx="3.5" ry="8"/><path d="M2 10 H18 M3.5 6 H16.5 M3.5 14 H16.5"/></svg>
        www.harvestlaneestates.com.au
      </li>
      <li>
        <svg viewBox="0 0 20 20" aria-hidden="true"><rect x="1.5" y="5" width="17" height="11" fill="var(--icon-blue)"/><path d="M1.5 5 L10 11.5 L18.5 5" fill="none" stroke="var(--card-navy)" stroke-width="1.5"/></svg>
        tom@harvestlaneestates.com.au
      </li>
      <li>
        <svg viewBox="0 0 20 20" aria-hidden="true"><path d="M5 2 L8 2 L9 6 L7 8 C8 11 9 12.5 12 14 L14 12 L18 13 L18 16 C18 17 17 18 16 18 C8 17 3 12 2 4 C2 3 3 2 5 2Z" fill="var(--icon-blue)"/></svg>
        0467 239 018
      </li>
    </ul>

    <p class="holder-name">Tom Carrick</p>
  </section>

</main>
</body>
</html>
```